Tarn - Stationary Design/Layout

We are a well established clothing design and manufacturing company (Tarn Sourcing) based in London UK, with our own factory in Bangladesh, supplying to many fashion retailers and brands. Our factory has very high environmental and ethical standards with people at its heart. Our quality of garments are second to none.
Our new logo has been proudly developed by the Pixel Guild community last month, we are now in the second phase and need the layout designed for our letterheads, double sided business cards, compliment slip and clothing ticket. Feel as creative as you like, but make sure it looks great!!
***The Logo - the logo design and colour is set and should NOT be changed and stay on a dark grey backround. The logo artwork to use is attached.
***Details to use for the business card:
Dorian Pelham
Direct Line: 020 7946 0158
dorian@tarnsourcing-example.com
Tarn Sourching Ltd.
57 - 59 Hollin Row
Camdon . Swindon
NW9 4QT
Switchboard: 020 7946 0274
Fax: 020 7946 0274
www.tarnsourcing-example.co.uk
***Details to use for the letterhead and compliment slip:
Tarn Sourching Ltd.
57 - 59 Hollin Row
Camdon . Swindon
NW9 4QT
Fax: 020 7946 0274
www.tarnsourcing-example.co.uk
***Details for Swing Ticket:
Size: 12cm height by 5.5cm width
One side need to have just the logo without the 'Sourcing', on the other it needs to stay blank

```html
<!DOCTYPE html>
<html lang="en">
<head>
<meta charset="utf-8">
<title>Tarn Sourcing – Stationery Set</title>
<link rel="stylesheet" href="https://fonts.googleapis.com/css2?family=Source+Sans+3:ital,wght@0,400;0,600;0,700;1,700&display=swap">
<style>
:root{
  --canvas:#aba9a9;
  --charcoal:#433e3d;
  --ice:#bbe0e7;
  --paper:#ffffff;
  --body-grey:#b3b3b3;
  --soft-grey:#8c8c8c;
  --window:#f1f1f1;
}
*{margin:0;padding:0;box-sizing:border-box}
html,body{width:1200px;height:900px;overflow:hidden}
body{background:var(--canvas);font-family:"Source Sans 3",Arial,sans-serif;position:relative}
.piece{position:absolute;overflow:hidden}
.piece>svg.shapes{position:absolute;inset:0;width:100%;height:100%}
.txt{position:absolute;white-space:nowrap;line-height:1.2}
.wordmark{position:absolute;color:var(--ice);font-weight:600;letter-spacing:2px;line-height:1}
.on-dark{color:var(--paper)}

/* Letterhead */
.letterhead{left:118px;top:37px;width:420px;height:593px;background:var(--paper)}
.lh-address{left:5px;top:4px;font-size:5.4px;font-weight:700;color:var(--paper)}
.lh-address p{margin:0}
.lh-address .gap{margin-top:6px}
.letterhead .wordmark{left:347px;top:19px;font-size:15px}
.salutation{left:46px;top:110px;font-size:10px;color:var(--soft-grey);letter-spacing:.5px}
.letter-body{position:absolute;left:30px;top:145px;width:362px;font-size:7.4px;line-height:9.6px;color:var(--body-grey);text-align:justify}
.letter-body p{text-indent:8px;margin-bottom:9px}
.sign-name{left:303px;top:435px;font-size:9px;color:var(--soft-grey)}
.sign-role{left:290px;top:446px;font-size:6.5px;color:var(--soft-grey)}
.signature{position:absolute;left:312px;top:457px;width:22px;height:16px;background:linear-gradient(#e4e4e4,#d2d2d2);border-radius:4px}
.footer-url{font-size:5.2px;font-weight:600;color:var(--paper)}
.letterhead .footer-url{left:174px;top:585px}

/* Swing tickets */
.ticket{background:var(--charcoal)}
.ticket-rect{width:99px;height:240px;top:45px}
.ticket-oval{width:95px;height:260px;top:320px;border-radius:48px}
.ticket .wordmark.base{left:3px;bottom:5px;font-size:24px;letter-spacing:1px}
.ticket .wordmark.upright{left:50%;top:50%;font-size:34px;letter-spacing:4px;transform:translate(-50%,-50%) rotate(90deg)}
.punch-line{position:absolute;right:0;width:47px;height:1px;background:#5a5554}

/* Business cards */
.card{width:171px;height:110px;background:var(--ice)}
.card-front{left:677px;top:328px}
.card-back{left:677px;top:461px}
.card-front .wordmark{left:116px;top:10px;font-size:11px;letter-spacing:1px}
.card-name{left:9px;top:40px;font-size:7.6px;font-weight:700;color:var(--ice)}
.card-direct{left:9px;top:53px;font-size:4.6px;color:var(--paper)}
.card-direct b{font-style:italic;font-weight:600}
.card-rule{position:absolute;left:86px;top:38px;width:1px;height:34px;background:#7d7877}
.card-address{left:90px;top:37px;font-size:4.6px;color:#d4d4d4;line-height:1.15}
.card-address b{color:var(--paper);font-weight:600}
.card-url{right:6px;bottom:3px;font-size:5px;font-weight:600;color:var(--charcoal)}
.card-back .wordmark{left:55px;top:47px;font-size:15px;letter-spacing:1.5px}

/* Compliment slip */
.comp-slip{left:121px;top:669px;width:420px;height:199px;background:var(--paper)}
.comp-slip .wordmark{left:14px;top:18px;font-size:16px;letter-spacing:1px}
.comp-title{left:159px;top:88px;font-size:11px;font-weight:700;font-style:italic;color:#a5a5a5;letter-spacing:.4px}
.comp-address{left:9px;top:132px;font-size:5.2px;color:var(--soft-grey);line-height:1.25}
.comp-address .gap{margin-top:6px}
.comp-slip .footer-url{left:174px;top:190px}

/* Envelope */
.envelope{left:585px;top:605px;width:438px;height:268px}
.env-address{left:8px;top:58px;font-size:5.4px;font-weight:700;color:var(--paper)}
.env-address .gap{margin-top:5px}
.envelope .wordmark{left:345px;top:65px;font-size:15px}
.env-window{position:absolute;left:264px;top:166px;width:146px;height:62px;border:1px solid #8a8a8a;border-radius:7px;background:var(--window)}
.envelope .footer-url{left:187px;top:260px;color:var(--paper)}
</style>
</head>
<body>

<!-- Letterhead -->
<section class="piece letterhead" aria-label="Letterhead">
  <svg class="shapes" viewBox="0 0 420 593" preserveAspectRatio="none">
    <path d="M0 0H420V12Q190 30 0 100Z" fill="var(--ice)"/>
    <path d="M0 0H420V6Q190 20 0 90Z" fill="var(--charcoal)"/>
    <path d="M0 560Q210 580 420 560V572Q210 582 0 572Z" fill="var(--ice)"/>
    <path d="M0 568Q210 580 420 568V593H0Z" fill="var(--charcoal)"/>
  </svg>
  <div class="txt lh-address">
    <p>Tarn Sourcing Ltd.</p>
    <p>57 - 59 Hollin Row, Camdon . Swindon NW9 4QT</p>
    <p class="gap">Switchboard: 020 7946 0274</p>
    <p>Fax: 020 7946 0274</p>
  </div>
  <div class="wordmark">TARN</div>
  <div class="txt salutation">Dear &nbsp;Sir / Maddame</div>
  <div class="letter-body">
    <p>Lorem ipsum dolor sit amet, consectetur adipiscing elit. Aenean ullamcorper tempor nisi, blandit ornare elit ultricies a. Sed non sem in elit tincidunt dignissim. Sed blandit mollis nisi, sed faucibus turpis feugiat convallis. Vestibulum ante ipsum primis in faucibus orci luctus et ultrices posuere cubilia Curae; Nullam turpis magna, euismod in commodo tristique, commodo non mi. Ut scelerisque, quam nec adipiscing cursus, justo nisl pellentesque purus, dictum imperdiet tortor augue eleifend tortor. Donec consequat libero ac lectus aliquam convallis facilisis enim luctus. Cras sodales tempor mauris a blandit. Nullam nulla ante, pharetra ut interdum eu, consectetur et augue. Aliquam mattis molestie malesuada. Proin vel eros velit, nec commodo arcu.</p>
    <p>In ultrices convallis eleifend. Nulla ac velit sed nibh tincidunt volutpat. Donec turpis massa, rhoncus sed dignissim non, condimentum sed tortor. Quisque ipsum arcu, condimentum eu pharetra ac, tincidunt ac nibh. Nulla accumsan molestie congue. Maecenas dictum pellentesque vestibulum. Nulla at convallis nibh. Nulla aliquam adipiscing eros mattis consequat. Fusce ultricies tincidunt nibh, quis fermentum nibh tempor dignissim. Nulla rutrum ligula sed neque convallis mattis. Duis feugiat neque non enim condimentum at dignissim orci mattis. Nulla vestibulum molestie ligula vel dapibus. Donec viverra, elit ac vestibulum viverra, tellus nunc vehicula nunc, in malesuada massa enim ut erat.</p>
    <p>Vivamus luctus posuere justo, eget blandit dui porttitor ac. Nam fermentum leo at elit consequat vel lobortis ligula eleifend. Nulla facilisi. Duis molestie viverra odio, sed pharetra ante lacinia in. Maecenas ullamcorper urna vel quam accumsan at luctus mauris egestas. Sed pulvinar arcu ut ipsum suscipit sit amet vulputate lorem dignissim. Cras a felis at ligula hendrerit rutrum congue non dolor. Proin ac turpis ut purus accumsan gravida sed in felis. Aenean tincidunt tincidunt laoreet. Quisque posuere sapien nec libero congue dapibus. Donec eleifend tempus tellus ut pretium. Etiam id arcu nisi. Duis suscipit luctus mi id semper. Sed lacinia porta lorem vitae faucibus. Sed non dolor mauris. Praesent eleifend eleifend sodales. Sed in quam in tellus ultricies tincidunt.</p>
  </div>
  <div class="txt sign-name">Alden Marsh</div>
  <div class="txt sign-role">marketing director</div>
  <div class="signature" role="img" aria-label="Handwritten signature"></div>
  <div class="txt footer-url">www.tarnsourcing-example.co.uk</div>
</section>

<!-- Swing tickets -->
<section class="piece ticket ticket-rect" style="left:650px" aria-label="Swing ticket front">
  <div class="wordmark base">TARN</div>
</section>
<section class="piece ticket ticket-rect" style="left:758px" aria-label="Swing ticket back"></section>
<section class="piece ticket ticket-rect" style="left:916px" aria-label="Swing ticket front, upright">
  <div class="wordmark upright">TARN</div>
</section>
<section class="piece ticket ticket-rect" style="left:1032px" aria-label="Swing ticket back, upright"></section>
<section class="piece ticket ticket-oval" style="left:925px" aria-label="Rounded swing ticket front">
  <div class="wordmark upright">TARN</div>
</section>
<section class="piece ticket ticket-oval" style="left:1043px" aria-label="Rounded swing ticket back">
  <span class="punch-line" style="top:22px"></span>
  <span class="punch-line" style="top:38px"></span>
  <span class="punch-line" style="top:200px"></span>
  <span class="punch-line" style="top:220px"></span>
</section>

<!-- Business card front -->
<section class="piece card card-front" aria-label="Business card front">
  <svg class="shapes" viewBox="0 0 171 110" preserveAspectRatio="none">
    <path d="M0 24Q100 6 171 0V70Q80 76 0 110Z" fill="var(--charcoal)"/>
    <path d="M0 110Q80 80 171 74V110Z" fill="var(--paper)"/>
  </svg>
  <div class="wordmark">TARN</div>
  <div class="txt card-name">Dorian Pelham</div>
  <div class="txt card-direct"><b>Direct Line:</b> 020 7946 0158<br>dorian@tarnsourcing-example.com</div>
  <span class="card-rule"></span>
  <div class="txt card-address">Tarn Sourching Ltd.<br>57 - 59 Hollin Row<br>Camdon . Swindon<br>NW9 4QT<br><b>Switchboard:</b> 020 7946 0274<br><b>Fax:</b> 020 7946 0274</div>
  <div class="txt card-url">www.tarnsourcing-example.co.uk</div>
</section>

<!-- Business card back -->
<section class="piece card card-back" aria-label="Business card back">
  <svg class="shapes" viewBox="0 0 171 110" preserveAspectRatio="none">
    <path d="M0 30Q70 4 171 6V80Q70 84 0 110Z" fill="var(--charcoal)"/>
  </svg>
  <div class="wordmark">TARN</div>
</section>

<!-- Compliment slip -->
<section class="piece comp-slip" aria-label="Compliment slip">
  <svg class="shapes" viewBox="0 0 420 199" preserveAspectRatio="none">
    <path d="M0 0H420V8Q200 28 0 82Z" fill="var(--ice)"/>
    <path d="M0 0H420V2Q200 18 0 72Z" fill="var(--charcoal)"/>
    <path d="M0 160Q210 185 420 160V170Q210 190 0 170Z" fill="var(--ice)"/>
    <path d="M0 168Q210 188 420 166V199H0Z" fill="var(--charcoal)"/>
  </svg>
  <div class="wordmark">TARN</div>
  <div class="txt comp-title">With Compliments</div>
  <div class="txt comp-address">Tarn Sourching Ltd.<br>57 - 59 Hollin Row, Camdon . Swindon NW9 4QT<div class="gap">Switchboard: 020 7946 0274</div>Fax: 020 7946 0274</div>
  <div class="txt footer-url">www.tarnsourcing-example.co.uk</div>
</section>

<!-- Envelope -->
<section class="piece envelope" aria-label="DL window envelope">
  <svg class="shapes" viewBox="0 0 438 268" preserveAspectRatio="none">
    <rect x="0" y="55" width="438" height="213" fill="var(--paper)"/>
    <path d="M0 55L80 0H380L438 55Z" fill="var(--charcoal)"/>
    <path d="M0 55H438V62Q200 80 0 160Z" fill="var(--ice)"/>
    <path d="M0 55H438V56Q200 70 0 150Z" fill="var(--charcoal)"/>
    <path d="M0 246Q219 262 438 246V254Q219 266 0 254Z" fill="var(--ice)"/>
    <path d="M0 252Q219 264 438 252V268H0Z" fill="var(--charcoal)"/>
  </svg>
  <div class="txt env-address">Tarn Sourcing Ltd.<br>57 - 59 Hollin Row, Camdon . Swindon NW9 4QT<div class="gap">Switchboard: 020 7946 0274</div>Fax: 020 7946 0274</div>
  <div class="wordmark">TARN</div>
  <div class="env-window"></div>
  <div class="txt footer-url">www.tarnsourcing-example.co.uk</div>
</section>

</body>
</html>
```